2018 - 2019 Academic Program & Schedule ofEvents

10 page booklet listing upcoming courses for Sept 2018- May 2019
Program guide showing members what the courses are for the upcoming year.
It gives the course description & learning objectives & CE credits offered for each lecture. Also gives date, time location, intended participants, course description & learning objectives

Please use the MVCR 2016-2017 & 2017-2018 program guides as reference. We don't want to use any actual photo of Hargrove, we would like something more modern and cleaner look like the above mentioned program guides.

Target Market(s)

Dentist

Industry/Entity Type

Dental

Font styles to use
Serif
Script

Colors
f37122

Requirements
Must have
• Must have our logo on front & back
• & "LORN logo on back
• Table of contents, Course title, Date, location, intended audience, Time, Speaker's name & Title
Nice to have
• Walter Hargrove quote

```html
<!DOCTYPE html>
<html lang="en">
<head>
<meta charset="utf-8">
<title>Academic Program &amp; Schedule of Events 2018–2019</title>
<link rel="stylesheet" href="https://fonts.googleapis.com/css2?family=Cormorant+Garamond:ital,wght@0,500;1,500&family=Noto+Serif:wght@400&family=Open+Sans:wght@400&family=Great+Vibes&display=swap">
<style>
  :root {
    --orange: #f37122;
    --orange-deep: #d85a1a;
    --peach: #f9c7aa;
    --peach-soft: #fde3d3;
    --ink: #2a2a2a;
    --white: #ffffff;
    --stage: #e4e4e4;
  }
  * { margin: 0; padding: 0; box-sizing: border-box; }
  html, body { width: 1200px; height: 797px; overflow: hidden; background: var(--stage); }
  .spread {
    position: absolute; left: 80px; top: 128px;
    width: 1040px; height: 540px; display: flex;
    box-shadow: 0 18px 40px rgba(0,0,0,.18);
  }
  .page { position: relative; width: 520px; height: 540px; overflow: hidden; }
  .back-cover { background: linear-gradient(160deg, var(--orange-deep) 0%, var(--orange) 60%, #ee6a24 100%); }
  .front-cover { background: var(--white); }
  .front-art { position: absolute; inset: 0; }

  .brand { position: absolute; font-family: "Cormorant Garamond", serif; }
  .brand-name {
    font-size: 13px; font-weight: 500; letter-spacing: .18em; text-transform: uppercase;
    line-height: 1.3;
  }
  .brand-tagline { font-style: italic; font-size: 12px; line-height: 1.3; margin-top: 4px; }
  .front-brand { right: 30px; top: 26px; text-align: left; color: var(--ink); width: 290px; }
  .back-brand { left: 44px; top: 395px; color: var(--white); width: 320px; }

  .title-block {
    position: absolute; left: 46px; top: 190px; width: 270px; text-align: center;
  }
  .title-amp {
    position: absolute; left: 50%; top: -46px; transform: translateX(-50%);
    font-family: "Great Vibes", cursive; font-size: 120px; color: var(--peach); opacity: .75;
    line-height: 1;
  }
  .title-main {
    position: relative; font-family: "Noto Serif", serif; font-size: 21px; line-height: 1.25;
    color: var(--ink);
  }
  .title-dates {
    position: relative; font-family: "Open Sans", sans-serif; font-size: 16px;
    color: var(--white); margin-top: 10px;
  }

  .contact {
    position: absolute; left: 44px; top: 470px; color: var(--white);
    font-family: "Cormorant Garamond", serif; font-size: 14px; line-height: 1.35;
  }
  .ce-badge { position: absolute; right: 36px; bottom: 40px; width: 56px; height: 56px;
    border: 2px solid var(--white); }
</style>
</head>
<body>
<main class="spread">
  <section class="page back-cover" aria-label="Back cover">
    <div class="brand back-brand">
      <p class="brand-name">Mill Valley Circle for Restorative Excellence</p>
      <p class="brand-tagline">Excellence through Dental Education<br>A Coastal Study Circle</p>
    </div>
    <address class="contact">
      218 Alder Lane, Suite C-4, Mill Valley, CA 94941<br>
      Tel: 415-555-0148 &nbsp;Fax: 415-555-0193 &nbsp;Email: mvcr@millvalleycircle.org
    </address>
    <div class="ce-badge" role="img" aria-label="LORN continuing education approval badge"></div>
  </section>

  <section class="page front-cover" aria-label="Front cover">
    <svg class="front-art" viewBox="0 0 520 540" width="520" height="540" aria-hidden="false">
      <defs>
        <linearGradient id="clinicTone" x1="0" y1="0" x2="1" y2="1">
          <stop offset="0" stop-color="#f4f5f7"/>
          <stop offset=".55" stop-color="#d9dde2"/>
          <stop offset=".8" stop-color="#f2b27c"/>
          <stop offset="1" stop-color="#e3e6ea"/>
        </linearGradient>
      </defs>
      <path class="cover-orange" fill="var(--orange)" d="M0,0 C170,72 340,112 520,122 L520,470 L330,540 L0,540 Z"/>
      <path class="cover-band" fill="var(--peach-soft)" opacity=".85" d="M300,128 L520,148 L520,162 L314,140 Z"/>
      <path class="cover-stripe" fill="var(--peach)" d="M0,350 C110,390 230,440 360,540 L330,540 C210,455 100,405 0,372 Z"/>
      <path class="cover-white-wedge" fill="var(--white)" d="M520,470 L520,540 L340,540 Z"/>
      <polygon role="img" aria-label="Photo of a bright modern dental treatment room with an orange patient chair" fill="url(#clinicTone)" points="330,142 520,162 520,500 300,462"/>
    </svg>

    <div class="brand front-brand">
      <p class="brand-name">Mill Valley Circle for Restorative Excellence</p>
      <p class="brand-tagline">Excellence through Dental Education<br>A Coastal Study Circle</p>
    </div>

    <div class="title-block">
      <span class="title-amp" aria-hidden="true">&amp;</span>
      <h1 class="title-main">Academic Program<br>Schedule of Events</h1>
      <p class="title-dates">Sept 2018 – May 2019</p>
    </div>
  </section>
</main>
</body>
</html>
```